Gullwrack Rum Liqueur Bottle Label

I will be launching a Rum Liqueur called Gullwrack Spiced Rum Liqueur. The bottle I have chosen to use is an TMV 500ml type and I have included a photo of it in the project brief. The bottle dimensions are height 193.5mm with diameter 85mm. There will be a cork closure, sealed with a heat shrink capsule. I require two labels for each bottle, a large rectangular label on the front with the product name, logo, label design and the bottle quantity which is 500ml. The front label should also contain the strength of the liqueur which is 25% vol. The rear label will contain the required UK legal information such as government health warning, number of UK units of alcohol as well as the place of bottling which is Wick, Caithness, Scotland. A barcode will also be on the rear label and I have added it as a jpg file. On my current homemade label I also have the following text on the rear label: "Due to the ferocious tides, currents and winds that shape the narrow stretch of water separating Caithness from the Orkney Islands in the far North of Scotland, it has become known to generations of sailors as "Gullwrack" and is the graveyard of countless number of ships. Gullwrack Spiced Rum Liqueur aims to capture the spirit of those brave men and women who have risked all on these treacherous shores". For the main front label I am keen for the designer to explore the themes of shipwreck, sea monsters, smuggling, pistols, diving helmets, heavy seas, sea stacks, high cliffs, sealife etc. I have included a story about a local smuggler called Peter Moray as an example of an inspirational theme. I currently also have a website regarding Caithness shipwrecks which can be found at www.gullwrack.example and which could provide some further ideas. My feeling is that the label design should be masculine and I would like to keep away from designs that would make the label costly to print. I have included a file with my current logo but please feel free to change its colour as required and to remove the word Gullwrack from the logo if you wish. I can supply the logo file in different formats such as jpg, ai, eps, pdf, png or psd. I also have the barcode in pdf, png or svg formats. The word Gullwrack is a registered trademark.I have also attached a photograph of my liqueur in an attempt to show the colour of the finished product and the bottle style.
Colors
Designer to choose colors to be used in the design.
Look and feel
Each slider illustrates characteristics of the customer's brand and the style your logo design should communicate.

```html
<!DOCTYPE html>
<html lang="en">
<head>
<meta charset="utf-8">
<title>Gullwrack Spiced Rum Liqueur – Front Label</title>
<link rel="stylesheet" href="https://fonts.googleapis.com/css2?family=Playfair+Display:wght@400;700;900&family=Pinyon+Script&display=swap">
<style>
  :root {
    --backdrop: #e9e9ea;
    --label-ground: #3b3b3c;
    --ink-light: #f3f3f1;
    --ink-soft: #cfcfcc;
    --art-dark: #2a2a2b;
    --art-mid: #6d6d6d;
  }
  html, body {
    margin: 0;
    padding: 0;
    width: 847px;
    height: 1200px;
    overflow: hidden;
    background: var(--backdrop);
  }
  .canvas {
    position: relative;
    width: 847px;
    height: 1200px;
  }
  .front-label {
    position: absolute;
    left: 84px;
    top: 95px;
    width: 680px;
    height: 1010px;
    background: var(--label-ground);
    color: var(--ink-light);
    font-family: "Playfair Display", Georgia, serif;
    text-align: center;
  }
  .tagline {
    position: absolute;
    top: 60px;
    left: 0;
    right: 0;
    margin: 0;
    font-weight: 900;
    font-size: 15px;
    letter-spacing: 1.5px;
    text-transform: uppercase;
  }
  .tagline-rule {
    position: absolute;
    top: 86px;
    left: 150px;
    width: 380px;
    height: 2px;
    background: var(--ink-light);
  }
  .shipwreck-art {
    position: absolute;
    top: 120px;
    left: 170px;
    width: 340px;
    height: 245px;
    border-radius: 40% 40% 6px 6px;
    background: radial-gradient(ellipse at 50% 75%, var(--art-mid) 0%, var(--art-dark) 70%, var(--label-ground) 100%);
  }
  .brand-name {
    position: absolute;
    top: 372px;
    left: 0;
    right: 0;
    margin: 0;
    font-weight: 900;
    font-size: 72px;
    line-height: 1;
    letter-spacing: 3px;
    text-transform: uppercase;
  }
  .flavour {
    position: absolute;
    top: 450px;
    left: 0;
    right: 0;
    margin: 0;
    font-family: "Pinyon Script", cursive;
    font-size: 64px;
    line-height: 1;
    color: var(--ink-soft);
  }
  .spirit-row {
    position: absolute;
    top: 520px;
    left: 0;
    right: 0;
    display: flex;
    align-items: center;
    justify-content: center;
    gap: 18px;
  }
  .spirit-rule {
    width: 60px;
    height: 12px;
    border-top: 3px solid var(--ink-light);
    border-bottom: 3px solid var(--ink-light);
    box-sizing: border-box;
  }
  .spirit-type {
    margin: 0;
    font-weight: 400;
    font-size: 132px;
    line-height: 1;
    letter-spacing: 2px;
  }
  .category {
    position: absolute;
    top: 650px;
    left: 0;
    right: 0;
    margin: 0;
    font-weight: 700;
    font-size: 28px;
    font-variant: small-caps;
    letter-spacing: 1px;
  }
  .flourish {
    position: absolute;
    left: 275px;
    width: 130px;
    height: 14px;
    background: linear-gradient(90deg, transparent, var(--ink-soft) 20%, var(--ink-soft) 80%, transparent);
    opacity: 0.45;
    border-radius: 7px;
  }
  .flourish-top { top: 727px; }
  .flourish-bottom { top: 897px; }
  .spec {
    position: absolute;
    left: 0;
    right: 0;
    margin: 0;
    font-size: 17px;
    letter-spacing: 1px;
    text-transform: uppercase;
    color: var(--ink-soft);
  }
  .spec-strength { top: 765px; }
  .spec-volume { top: 850px; }
  .spec-divider {
    position: absolute;
    top: 812px;
    left: 318px;
    width: 44px;
    height: 12px;
    border-top: 2px solid var(--ink-soft);
    border-bottom: 2px solid var(--ink-soft);
    box-sizing: border-box;
  }
</style>
</head>
<body>
<div class="canvas">
  <section class="front-label">
    <p class="tagline">For bravest men and women</p>
    <div class="tagline-rule"></div>

    <div class="shipwreck-art" role="img" aria-label="Illustration of a wrecked sailing ship with a sea serpent rising from the waves"></div>

    <h1 class="brand-name">Gullwrack</h1>
    <p class="flavour">Spiced</p>

    <div class="spirit-row">
      <span class="spirit-rule"></span>
      <h2 class="spirit-type">RUM</h2>
      <span class="spirit-rule"></span>
    </div>

    <p class="category">Liqueur</p>

    <div class="flourish flourish-top" role="img" aria-label="Decorative scroll flourish"></div>
    <p class="spec spec-strength">25% vol</p>
    <div class="spec-divider"></div>
    <p class="spec spec-volume">500ml</p>
    <div class="flourish flourish-bottom" role="img" aria-label="Decorative scroll flourish"></div>
  </section>
</div>
</body>
</html>
```